Small legal and financial translation company needs Squarespace website, brochure and logo

Hello,
We are KLV Services (www.klvservices-example.com), a boutique legal and financial translation company. We offer our services mainly to Spanish customers. Our primary line of business is the translation of financial statements, but we translate a wide variety legal and financial texts.
The project we are offering comprises three parts: a redo of the current website, an informational brochure for potential customer and a logo design. These three parts should provide a consistent image. We would develop content soon.
We are looking for a website that would look like a typical law firm website, nothing too fancy. Right now, it is in English, Spanish and French, although the new site need only be in English and Spanish. There must be good toggling between the English and Spanish versions. There would be no need for tie-ins to social media and it would not contain a blog. Basically, a static site. We aren't interesting in driving traffic to the site or SEO, as we will contact nearly all potential customers beforehand. The website must be built in Squarespace to enable a smooth transition. The content would be similar to the current page, we'll be working on the exact content, but a rough draft is attached.
The brochure will be some three pages and would introduce the company to potential customers, using similar images as the website and the logo to be designed.
The only specifications for the logo is, as the website and brochure, it convey a sense of security and trust.
Feel free to ask with any questions as this is the first time we have used this platform.
Thank you!

I've added a more or less final version for the text in the brochure and updated the brief. Added Wednesday, June 10, 2015

Target Market(s)

Spanish law firms, auditors, accountants, banks, investment firms

Industry/Entity Type

Finance

Logo Text

KLV Services

Number of Pages Required

5+ page

Font styles to use
Serif

Requirements
Must have
• The website must be built in Squarespace and have a good option to toggle between English and Spanish versions.
• Brochure must be in both English and Spanish, I'm attaching a rough draft of the information that it will probably have. This should give an idea about what to include and the spacing. I will update it to include the final information.
Nice to have
• Would be nice to have some quality finance- and legal-related images
Should not have
• Vibrant colours

```html
<!DOCTYPE html>
<html lang="en">
<head>
<meta charset="utf-8">
<title>KLV Services — Who we are</title>
<link rel="stylesheet" href="https://fonts.googleapis.com/css2?family=EB+Garamond:wght@400;700&family=Montserrat:wght@600;800&family=Bebas+Neue&display=swap">
<style>
  :root {
    --page-bg: #181818;
    --footer-bg: #333333;
    --teal: #2a8f99;
    --teal-nav: #3f9bb0;
    --logo-blue: #9fd3ec;
    --text-light: #ececec;
    --text-muted: #8c8c8c;
    --white: #ffffff;
    --band: rgba(240, 240, 240, 0.82);
    --band-text: #2b2b2b;
  }
  * { margin: 0; padding: 0; box-sizing: border-box; }
  html, body { width: 1159px; height: 1200px; overflow: hidden; background: var(--page-bg); }
  .page { position: relative; width: 1159px; height: 1200px; background: var(--page-bg); font-family: "EB Garamond", Georgia, serif; }

  .hero {
    position: absolute; left: 0; top: 0; width: 1159px; height: 431px;
    background:
      linear-gradient(160deg, rgba(20,20,20,.85) 0%, rgba(20,20,20,0) 32%),
      linear-gradient(200deg, rgba(30,30,30,.8) 0%, rgba(30,30,30,0) 28%),
      linear-gradient(180deg, #9a9a9a 0%, #6e6e6e 45%, #3a3a3a 100%);
  }
  .brand {
    position: absolute; left: 16px; top: 38px;
    font-family: "EB Garamond", Georgia, serif; font-weight: 400;
    font-size: 30px; color: var(--logo-blue); letter-spacing: .5px;
  }
  .top-nav { position: absolute; right: 12px; top: 53px; display: flex; gap: 26px; }
  .top-nav a {
    font-family: "Montserrat", Arial, sans-serif; font-weight: 600; font-size: 11px;
    letter-spacing: 1.6px; color: var(--white); text-decoration: none;
  }
  .hero-title {
    position: absolute; left: 0; top: 190px; width: 1159px; text-align: center;
    font-family: "Montserrat", Arial, sans-serif; font-weight: 800; font-size: 52px;
    letter-spacing: 3px; color: var(--white); padding-left: 0; text-indent: 0;
  }
  .hero-title span { position: relative; left: 0; }

  .side-nav { position: absolute; left: 175px; top: 510px; }
  .side-nav .lang { font-size: 19px; color: var(--teal); margin-bottom: 6px; }
  .side-nav ul { list-style: none; }
  .side-nav li {
    font-family: "Bebas Neue", Impact, sans-serif; font-size: 17px; letter-spacing: 1.3px;
    color: var(--text-muted); height: 31.7px; line-height: 24px;
  }
  .side-nav li.current { color: var(--teal-nav); }

  .content { position: absolute; left: 391px; top: 510px; width: 600px; }
  .content h1 { font-weight: 400; font-size: 30px; color: var(--teal); margin-bottom: 14px; }
  .content p { font-size: 16.5px; line-height: 20.4px; letter-spacing: 1.05px; color: var(--text-light); }
  .content strong { font-weight: 700; }

  .stats { position: absolute; left: 392px; top: 769px; display: flex; gap: 11px; }
  .stat { position: relative; width: 191px; height: 125px; overflow: hidden; }
  .stat-photo { position: absolute; inset: 0; background: linear-gradient(180deg, #b8b8b8 0%, #7a7a7a 50%, #2e2e2e 100%); }
  .stat-band {
    position: absolute; left: 0; width: 191px; background: var(--band);
    text-align: center; color: var(--band-text);
  }
  .stat-band .big { display: block; font-size: 21px; line-height: 22px; color: var(--teal); }
  .stat-band .small { display: block; font-size: 11px; line-height: 12px; }

  .footer-band { position: absolute; left: 0; top: 1120px; width: 1159px; height: 53px; background: var(--footer-bg); }
</style>
</head>
<body>
<div class="page">
  <header class="hero" role="img" aria-label="Black and white photograph looking up at city skyscrapers">
    <div class="brand">KLV Services</div>
    <nav class="top-nav"><a href="#">HOME</a><a href="#">ENGLISH</a><a href="#">SPANISH</a></nav>
    <h2 class="hero-title">WHO WE ARE</h2>
  </header>

  <aside class="side-nav">
    <div class="lang">English</div>
    <ul>
      <li class="current">Who we are</li>
      <li>Benefits</li>
      <li>Legal translation</li>
      <li>Financial translation</li>
      <li>Translation specialist</li>
      <li>Pricing</li>
      <li>Contact</li>
    </ul>
  </aside>

  <main class="content">
    <h1>Who we are</h1>
    <p>We are a small, highly qualified group of professionals with <strong>backgrounds in law, financial services and translation</strong> that boasts experience in global consulting and auditing firms, law firms and companies from a <strong>wide cross-section of industries</strong>. Sensitive to the workings of the world of finance, accounting and law, we are <strong>detail-oriented experts</strong> striving to facilitate understanding among investors, companies and international organisations:</p>
  </main>

  <section class="stats">
    <div class="stat">
      <div class="stat-photo" role="img" aria-label="Black and white photograph of office towers"></div>
      <div class="stat-band" style="top:42px;height:50px;padding-top:6px;">
        <span class="big">over 30 years</span><span class="small">of combined experience</span>
      </div>
    </div>
    <div class="stat">
      <div class="stat-photo" role="img" aria-label="Black and white photograph of a city street"></div>
      <div class="stat-band" style="top:30px;height:62px;padding-top:2px;">
        <span class="big">serving</span><span class="small">Big 4 firms, leading international law firms and banks and Meridia 35 listings and blue chips</span>
      </div>
    </div>
    <div class="stat">
      <div class="stat-photo" role="img" aria-label="Black and white photograph of skyscrapers"></div>
      <div class="stat-band" style="top:42px;height:50px;padding-top:4px;">
        <span class="big">over a milion</span><span class="small">words translated annually</span>
      </div>
    </div>
  </section>

  <footer class="footer-band"></footer>
</div>
</body>
</html>
```